Internation Biosecurity Business that needs a to design a Label for Itch relief product

Brand Name: Halcyon Cutis
I have a logo.
Label sign is 2.5 x 5.5
Label will be printed on clear vinyl.
The bottle to receive this label is colour of white.

I like the look of a label with the bottom starting off as a solid colour and transitioning to white at the top. But if you have something else you would like to try I am going to be open to it.
What ever colours and design you create it must reflect a natural, clean, soothing feeling. This colour could stop on the main panel or continue across to the side panel.
Primary panel size 2.5 x 3, Back side panel size 2.5 x 2.5 for a total size of 2.5 x 5.5 inches
Text on primary panel:
logo (which will have the brand name Halcyon Cutis incorporated in it)
- Itch Relief (main message to stand out big ! )
- from Psoriasis, Eczema, Dermatitis (secondary message) but also must stand out but less than "Itch Relief"
- Natural, Nontoxic, Non- medicated (place at bottom
- 100ml (Bottle size)
I am looking for a symbol to be in the background on the main panel or as a water mark on the back panel. This symbol will have a very light outline so it hardly noticed. The symbol I had in mind was the "Liberty Bell" because it stands for freedom. My hope is this will convey a subliminal message of freedom, liberty and trust. You can be free to select a different symbol or nothing at all.

The logo that I have attached Halcyon Cutis but these colours must be changed to new colours which must harmonize with the colour you select for the over all label.
I will be coming out with many more labels in this "Halcyon" line so the designer that creates the winning art work will be hired in the not-so- distant future for all new labels.
The product is water based and sprayed on. Active ingredient is HOCL. You cannot harm yourself even if it get in your eyes. Our products comes at treating the problems from a Holistic approach and not from a chemical medicated approach.
Company Name: PuraVerde Remedies Inc. Box 4587, Innisfail Alberta, R2K 7M3 1 800-915 -2706 Made in Canada (UPC Code: 6 51934 80472 1)

Industry/Entity Type

Business

Colors
886aae
b7a5cd
e4daeb

Requirements
Must have
• Final Graphic files must be in vector/eps format! I need you to enlarge it more because I can not read or see label text or see how you have placed the bell even at the 150%. The situation is that I will be using the winning design as a template for Halcyon Peak, Halcyon Cutis and Halcyon Vita. Each of these categories may have 2 - 4 different products in them. What will distinguished these categories will be a different colour at the bottom of the label. For the Halcyon Cutis label I have chosen the mauve or light purple. Light green of Halcyon Peak, Light blue for Halcyon Vita.
• At the bottom of the label let remove "Antimicrobial Cleanser". One of the problems we Canada's manufacturers have is that some keg words on our labels mush me in French and your present design does not lend itself to incorporating French. We may be able to have a French label underneath the English label, However, The words "Itch Relief" and the phase "Natural, Nontoxic, Non-Medicated" would need to be in French, at a reduced size, so we may need some space. French for Itch Relief is: D mangeaison de secours (place very small under "Itch Relief") French for Natural, Nontoxic, Non-medicated is : Naturel, Non toxque, Non meddicamenteux, place very small under the English.
Should not have
• The same colours that are in the Halcyon Cutis Logo. I want different colours.

```html
<!DOCTYPE html>
<html lang="en">
<head>
<meta charset="utf-8">
<title>Halcyon Cutis – Itch Relief Label</title>
<link rel="stylesheet" href="https://fonts.googleapis.com/css2?family=Oswald:wght@200;300;400;500&display=swap">
<style>
  :root {
    --purple: #886aae;
    --purple-text: #8563b3;
    --lavender: #b7a5cd;
    --lilac-pale: #e4daeb;
    --mauve-deep: #a58fc2;
    --white: #ffffff;
    --watermark: rgba(200, 195, 210, 0.28);
  }
  * { margin: 0; padding: 0; box-sizing: border-box; }
  html, body {
    width: 1200px;
    height: 1200px;
    overflow: hidden;
    background: var(--white);
  }
  .label {
    position: relative;
    width: 1200px;
    height: 1200px;
    overflow: hidden;
    font-family: "Oswald", "Arial Narrow", sans-serif;
    background: linear-gradient(to bottom,
      var(--white) 0%,
      var(--white) 30%,
      var(--lilac-pale) 55%,
      var(--lavender) 85%,
      var(--mauve-deep) 100%);
  }
  .watermark {
    position: absolute;
    left: -60px;
    top: 20px;
    width: 360px;
    height: 560px;
    border-radius: 45% 45% 20% 20%;
    background: radial-gradient(ellipse at 50% 40%, var(--watermark), rgba(220,215,225,0) 72%);
  }
  .brand {
    position: absolute;
    top: 60px;
    left: 0;
    width: 100%;
    display: flex;
    justify-content: center;
    align-items: center;
    gap: 22px;
  }
  .brand-mark {
    width: 74px;
    height: 74px;
    background: var(--lavender);
  }
  .brand-name {
    font-weight: 400;
    font-size: 72px;
    line-height: 1;
    color: var(--purple);
    letter-spacing: 1px;
  }
  .headline {
    position: absolute;
    left: 0;
    width: 100%;
    text-align: center;
    font-weight: 300;
    font-size: 236px;
    line-height: 1;
    color: var(--purple-text);
    letter-spacing: 4px;
    transform: scaleY(1.21);
    transform-origin: top center;
  }
  .headline-itch { top: 151px; }
  .headline-relief { top: 411px; }
  .headline-fr {
    position: absolute;
    top: 696px;
    left: 0;
    width: 100%;
    text-align: center;
    font-weight: 300;
    font-size: 24px;
    line-height: 1;
    color: var(--purple-text);
    letter-spacing: 2px;
  }
  .conditions-band {
    position: absolute;
    top: 730px;
    left: 0;
    width: 100%;
    height: 80px;
    background: var(--purple);
    display: flex;
    align-items: center;
    justify-content: center;
  }
  .conditions {
    font-weight: 500;
    font-size: 52px;
    line-height: 1;
    color: var(--white);
    letter-spacing: 0.5px;
  }
  .claims {
    position: absolute;
    top: 926px;
    left: 0;
    width: 100%;
    text-align: center;
    font-weight: 300;
    font-size: 36px;
    line-height: 1.2;
    color: var(--purple-text);
    letter-spacing: 1px;
  }
  .claims-fr {
    position: absolute;
    top: 978px;
    left: 0;
    width: 100%;
    text-align: center;
    font-weight: 300;
    font-size: 22px;
    line-height: 1;
    color: var(--purple-text);
    letter-spacing: 1px;
  }
  .volume {
    position: absolute;
    top: 1036px;
    left: 0;
    width: 100%;
    text-align: center;
    font-weight: 500;
    font-size: 74px;
    line-height: 1;
    color: var(--purple-text);
    letter-spacing: 1px;
  }
</style>
</head>
<body>
  <main class="label">
    <div class="watermark" role="img" aria-label="Faint bell watermark outline"></div>

    <header class="brand">
      <span class="brand-mark"></span>
      <span class="brand-name">Halcyon Cutis</span>
    </header>

    <h1>
      <span class="headline headline-itch">ITCH</span>
      <span class="headline headline-relief">RELIEF</span>
    </h1>
    <p class="headline-fr" lang="fr">DÉMANGEAISON DE SECOURS</p>

    <div class="conditions-band">
      <p class="conditions">FROM PSORIASIS, ECZEMA, DERMATITIS</p>
    </div>

    <p class="claims">NATURAL, NONTOXIC, NON-MEDICATED</p>
    <p class="claims-fr" lang="fr">NATUREL, NON TOXIQUE, NON MÉDICAMENTEUX</p>

    <p class="volume">100ML</p>
  </main>
</body>
</html>
```